Business / Discount Card

Looking to create a 2 sided business card. Front side to say "Thanks for flying with Skyward Drifts" then have link to "In-Flight Photos, www.skywarddrifts-example.com.au, password: skyward" Back side of card to have company logo, phone number, facebook & instagram logo and #skywarddrifts. Also included on this side will be discount text "Book again and save 10%. Use discount code: skyward10"Round Corner Card Templates are attached. Please ensure dimensions are correct.Thanks,

Font styles to use
Sans Serif

Colors
33a6d7
ffffff
000000

Requirements
Must have
• Logo
• Blue, White and Black color scheme

```html
<!DOCTYPE html>
<html lang="en">
<head>
<meta charset="utf-8">
<title>Skyward Drifts – Discount Card</title>
<link rel="stylesheet" href="https://fonts.googleapis.com/css2?family=Oswald:wght@600&family=Roboto:wght@400;500&family=Pacifico&display=swap">
<style>
  :root {
    --sky-blue: #33a6d7;
    --white: #ffffff;
    --black: #000000;
    --card-black: #0b0b0b;
    --backdrop: #e9eef1;
  }
  * { box-sizing: border-box; margin: 0; padding: 0; }
  html, body { width: 1200px; height: 1000px; overflow: hidden; }
  body {
    background: var(--backdrop);
    position: relative;
    font-family: "Roboto", Arial, sans-serif;
  }
  .card {
    position: absolute;
    top: 350px;
    width: 480px;
    height: 300px;
    border-radius: 22px;
    overflow: hidden;
    box-shadow: 0 10px 30px rgba(0,0,0,0.18);
  }
  .card-front { left: 90px; background: var(--white); }
  .card-back { left: 630px; background: var(--card-black); color: var(--white); }

  .front-waves { position: absolute; inset: 0; width: 100%; height: 100%; }

  .front-mark {
    position: absolute; left: 34px; top: 30px;
    width: 46px; height: 46px; border-radius: 50%;
    background: var(--sky-blue);
  }
  .thanks {
    position: absolute; left: 0; right: 0; top: 64px;
    text-align: center;
    font-family: "Oswald", "Arial Narrow", sans-serif;
    font-weight: 600; text-transform: uppercase;
    color: var(--black); line-height: 1;
  }
  .thanks-line { display: block; font-size: 30px; letter-spacing: 0.5px; }
  .thanks-with {
    display: block;
    font-family: "Pacifico", cursive;
    font-size: 22px; text-transform: none;
    color: var(--sky-blue); margin: 4px 0 6px;
  }
  .photo-link {
    position: absolute; left: 0; right: 0; bottom: 24px;
    text-align: center; color: var(--black);
  }
  .photo-link-title {
    font-family: "Oswald", "Arial Narrow", sans-serif;
    font-weight: 600; font-size: 17px; text-transform: uppercase;
  }
  .photo-link-url { font-size: 14px; font-weight: 500; }

  .brand {
    position: absolute; left: 0; right: 0; top: 52px;
    display: flex; align-items: center; justify-content: center; gap: 14px;
  }
  .brand-dot { width: 40px; height: 40px; border-radius: 50%; background: var(--sky-blue); }
  .brand-name { font-size: 42px; font-weight: 500; color: var(--sky-blue); }
  .phone {
    position: absolute; left: 0; right: 0; top: 138px;
    text-align: center; font-size: 20px;
  }
  .discount {
    position: absolute; left: 0; right: 0; top: 172px;
    text-align: center; font-size: 15px; color: var(--sky-blue);
  }
  .discount strong { color: var(--white); font-weight: 500; }
  .social {
    position: absolute; left: 0; right: 0; top: 216px;
    display: flex; align-items: center; justify-content: center; gap: 12px;
  }
  .social-dot { width: 28px; height: 28px; border-radius: 50%; background: var(--sky-blue); }
  .hashtag { font-size: 21px; }
</style>
</head>
<body>

<section class="card card-front" aria-label="Card front">
  <svg class="front-waves" viewBox="0 0 480 300" preserveAspectRatio="none" aria-hidden="true">
    <path d="M0 150 C 140 175, 300 210, 480 190 L480 300 L0 300 Z" fill="var(--black)"/>
    <path d="M0 212 C 150 205, 320 225, 480 265 L480 300 L0 300 Z" fill="var(--white)"/>
    <path d="M0 220 C 150 213, 320 233, 480 273 L480 300 L0 300 Z" fill="var(--sky-blue)"/>
  </svg>
  <div class="front-mark"></div>
  <h1 class="thanks">
    <span class="thanks-line">Thanks for flying</span>
    <span class="thanks-with">with</span>
    <span class="thanks-line">Skyward Drifts</span>
  </h1>
  <div class="photo-link">
    <p class="photo-link-title">In-Flight Photos</p>
    <p class="photo-link-url">www.skywarddrifts-example.com.au, password: skyward</p>
  </div>
</section>

<section class="card card-back" aria-label="Card back">
  <div class="brand">
    <span class="brand-dot"></span>
    <span class="brand-name">Skyward Drifts</span>
  </div>
  <p class="phone">1300 555 019</p>
  <p class="discount">Book again and save <strong>10%</strong>. Use discount code: <strong>skyward10</strong></p>
  <div class="social">
    <span class="social-dot"></span>
    <span class="hashtag">#skywarddrifts</span>
    <span class="social-dot"></span>
  </div>
</section>

</body>
</html>
```